E-customs by VELDAX

Our new site consists of: - Publish a regulatory watch by allowing access to the latest regulations and news specific to its field of activity. It will be asked when registering to choose 2 areas of activity from a predefined list - Make available the customs documents (DAU) and reverse charge reports - Establishment of a personal space project on which we bring our customs expertise to the client in order to change the management of its flows, this space will also allow him to keep his authorizations, RTC etc - Exhibit statistical tools (graph, curves ...) from the customs documents loaded on the site Our targets are our current customers, our prospects (importers, exporters) There will therefore be a personal secure access to create. The colors and tones must remain on the logo. "Logical" contrasts are appreciated.

Target Market(s)

importer / exporters

Font styles to use
Serif
Sans Serif

Colors

Designer to choose colors to be used in the design.

Requirements
Must have
• the following topics: - regulatory watch (modern newspaper template) - pdf file release (summary)
Nice to have
• a modern and functional design

```html
<!DOCTYPE html>
<html lang="en">
<head>
<meta charset="utf-8">
<title>VELDAX – E-customs</title>
<link href="https://fonts.googleapis.com/css2?family=Poppins:wght@500;600;700;800&family=Open+Sans:wght@400;600&display=swap" rel="stylesheet">
<style>
:root{
  --navy:#1b3b8f;
  --navy-dark:#12296a;
  --magenta:#d3176e;
  --ink:#1a1a1a;
  --muted:#8a8a8a;
  --grey-bg:#f1f1f1;
  --white:#ffffff;
  --footer:#1d1d20;
  --footer-text:#bdbdbd;
}
*{box-sizing:border-box;margin:0;padding:0}
html,body{width:1200px;height:3628px;overflow:hidden}
body{font-family:"Open Sans",Arial,sans-serif;color:var(--ink);background:var(--white)}
.container{width:940px;margin:0 auto;position:relative}
h2.section-title{font-family:"Poppins",Arial,sans-serif;font-weight:700;font-size:30px;line-height:40px;color:var(--ink)}

/* header */
.site-header{height:100px;background:var(--white);display:flex;align-items:center}
.site-header .container{display:flex;align-items:center;justify-content:space-between}
.brand{display:flex;align-items:center;gap:10px;font-family:"Poppins",Arial,sans-serif;font-weight:700;font-size:26px;color:var(--ink)}
.brand-dot{width:26px;height:26px;border-radius:50%;background:var(--magenta)}
.main-nav{display:flex;align-items:center;gap:30px}
.main-nav a{font-family:"Poppins",Arial,sans-serif;font-size:13px;font-weight:500;color:#333;text-decoration:none;letter-spacing:.3px;padding:6px 0}
.main-nav a.active{color:var(--navy);border-bottom:2px solid var(--navy)}
.main-nav a.btn-download{background:var(--navy);color:var(--white);padding:10px 18px;font-weight:600}

/* hero */
.hero{height:440px;position:relative;background:linear-gradient(120deg,#3a4e6e 0%,#8a7d70 38%,#c8a27a 55%,#4a5d7e 80%,#2b3550 100%)}
.hero-panel{position:absolute;left:148px;top:60px;width:332px;height:280px;background:rgba(20,30,60,.72);padding:28px 26px;color:var(--white)}
.tag{display:inline-block;background:var(--navy);color:var(--white);font-family:"Poppins",Arial,sans-serif;font-size:10px;font-weight:600;padding:4px 10px;letter-spacing:.5px}
.hero-panel h1{font-family:"Poppins",Arial,sans-serif;font-weight:800;font-size:34px;line-height:40px;margin-top:18px}
.hero-panel p{font-size:18px;line-height:26px;margin-top:8px}
.btn{display:inline-block;background:var(--navy);color:var(--white);font-family:"Poppins",Arial,sans-serif;font-size:10px;font-weight:600;padding:7px 12px;text-decoration:none;letter-spacing:.3px}
.hero-panel .btn{margin-top:26px;font-size:12px;padding:10px 18px}
.dots{position:absolute;left:560px;top:404px;display:flex;gap:8px}
.dots span{width:8px;height:8px;border-radius:50%;background:rgba(255,255,255,.55)}
.dots span.on{background:var(--white)}

/* sections */
.latest{height:1000px;background:var(--grey-bg);padding-top:52px}
.featured{height:540px;background:var(--white);padding-top:40px}
.recent{height:560px;background:var(--grey-bg);padding-top:50px}
.popular{height:660px;background:var(--white);padding-top:50px}

.latest-grid{margin-top:28px;display:grid;grid-template-columns:repeat(4,1fr);grid-template-rows:388px 400px;gap:12px}
.span2{grid-column:span 2}

.card{background:var(--white);display:flex;flex-direction:column;box-shadow:0 1px 3px rgba(0,0,0,.06)}
.card .photo{position:relative;flex:none}
.card .body{padding:14px 16px 16px;display:flex;flex-direction:column;flex:1}
.date{font-size:10px;color:var(--muted);letter-spacing:.3px}
.card h3{font-family:"Poppins",Arial,sans-serif;font-weight:700;font-size:12.5px;line-height:17px;margin-top:6px}
.card p{font-size:11px;line-height:16px;color:var(--muted);margin-top:8px}
.card .btn{align-self:flex-start;margin-top:auto}

.badge{position:absolute;left:12px;top:12px;background:var(--white);color:var(--ink);font-size:10px;padding:3px 8px}

.feature-card{position:relative;color:var(--white);display:flex;flex-direction:column;justify-content:flex-end;padding:0 28px 28px}
.feature-card .shade{position:absolute;inset:0;background:linear-gradient(180deg,rgba(0,0,0,0) 45%,rgba(0,0,0,.75) 100%)}
.feature-card > *:not(.photo-fill):not(.shade){position:relative}
.photo-fill{position:absolute;inset:0}
.feature-card .date-pill{align-self:flex-start;background:var(--white);color:var(--ink);font-size:10px;padding:4px 10px}
.feature-card h3{font-family:"Poppins",Arial,sans-serif;font-weight:700;font-size:20px;line-height:26px;margin-top:12px}
.feature-card p{font-size:12px;line-height:18px;margin-top:8px;color:#e4e4e4}

.featured-grid{margin-top:20px;display:grid;grid-template-columns:repeat(4,1fr);gap:14px;height:380px}
.featured-grid .photo{height:140px}

.recent-head{display:flex;justify-content:space-between;align-items:center}
.arrows{display:flex;gap:18px}
.recent-grid{margin-top:10px;display:grid;grid-template-columns:repeat(3,1fr);gap:20px;height:400px}
.recent-grid .photo{height:160px}
.recent-grid .body{padding:22px 22px 24px}
.recent-grid h3{font-size:16px;line-height:22px}
.recent-grid p{font-size:12px;line-height:17px}

.popular-grid{margin-top:22px;display:grid;grid-template-columns:448px 1fr 1fr;grid-template-rows:240px 240px;gap:8px 12px;height:488px}
.popular-grid .big{grid-row:span 2}
.popular-grid .photo{height:150px}
.popular-grid .body{padding:10px 12px}
.popular-grid h3{margin-top:0}

/* footer */
.site-footer{height:328px;background:var(--footer);text-align:center;color:var(--footer-text);padding-top:58px}
.site-footer .brand{justify-content:center;color:var(--white);font-size:28px}
.footer-nav{margin-top:30px;display:flex;justify-content:center;gap:14px;font-family:"Poppins",Arial,sans-serif;font-size:12px}
.footer-nav a{color:var(--white);text-decoration:none}
.footer-nav .sep{color:#777}
.social{margin-top:22px;display:flex;justify-content:center;gap:12px}
.social span{width:28px;height:28px;border-radius:50%;background:var(--navy)}
.copyright{margin-top:36px;font-size:11px;color:#8d8d8d}
</style>
</head>
<body>

<header class="site-header">
  <div class="container">
    <div class="brand"><span class="brand-dot"></span>Veldax</div>
    <nav class="main-nav">
      <a href="#" class="active">HOME</a>
      <a href="#">ABOUT US</a>
      <a href="#">VIDEOS</a>
      <a href="#">BLOG</a>
      <a href="#">CONTACT US</a>
      <a href="#" class="btn-download">DOWNLOAD PDF</a>
    </nav>
  </div>
</header>

<section class="hero" role="img" aria-label="Stacked shipping boxes on a glowing logistics conveyor">
  <div class="hero-panel">
    <span class="tag">FEATURED POSTS</span>
    <h1>CUSTOMS<br>DOCUMENT</h1>
    <p>Lorem Ipsum is simply dummy text of the printing...</p>
    <a href="#" class="btn">READ MORE</a>
  </div>
  <div class="dots"><span></span><span class="on"></span><span></span><span></span></div>
</section>

<section class="latest">
  <div class="container">
    <h2 class="section-title">Latest Blog</h2>
    <div class="latest-grid">
      <article class="feature-card span2">
        <div class="photo-fill" role="img" aria-label="Cargo aircraft being loaded on the apron" style="background:linear-gradient(160deg,#c9d3dc,#7f8a96 55%,#3f4650)"></div>
        <div class="shade"></div>
        <span class="date-pill">10 JUL 2019</span>
        <h3>LOREM IPSUM IS SIMPLY DUMMY TEXT.</h3>
        <p>Sed ut perspiciatis unde omnis iste natus error sit voluptatem accusantium doloremque.</p>
      </article>
      <article class="card">
        <div class="photo" style="height:196px;background:linear-gradient(160deg,#6d7fa0,#3b4a6c)" role="img" aria-label="Warehouse aisles with stacked pallets"></div>
        <div class="body">
          <span class="date">10 JUL 2019</span>
          <h3>LOREM IPSUM IS SIMPLY DUMMY TEXT.</h3>
          <p>Sed ut perspiciatis unde omnis iste natus error sit voluptatem accusantium doloremque.</p>
          <a href="#" class="btn">READ MORE</a>
        </div>
      </article>
      <article class="card">
        <div class="photo" style="height:196px;background:linear-gradient(160deg,#d8b48a,#8a6a48)" role="img" aria-label="Cardboard parcels stacked in a storeroom"></div>
        <div class="body">
          <span class="date">10 JUL 2019</span>
          <h3>LOREM IPSUM IS SIMPLY DUMMY TEXT.</h3>
          <p>Sed ut perspiciatis unde omnis iste natus error sit voluptatem accusantium doloremque.</p>
          <a href="#" class="btn">READ MORE</a>
        </div>
      </article>
      <article class="card">
        <div class="photo" style="height:196px;background:linear-gradient(160deg,#f0b070,#8b6aa8 60%,#3e4a86)" role="img" aria-label="Cargo plane and ship at sunset"></div>
        <div class="body">
          <span class="date">10 JUL 2019</span>
          <h3>LOREM IPSUM IS SIMPLY DUMMY TEXT.</h3>
          <p>Sed ut perspiciatis unde omnis iste natus error sit voluptatem accusantium doloremque.</p>
          <a href="#" class="btn">READ MORE</a>
        </div>
      </article>
      <article class="card">
        <div class="photo" style="height:196px;background:linear-gradient(160deg,#c49a6c,#6a5440)" role="img" aria-label="Hands holding a parcel and a tablet"></div>
        <div class="body">
          <span class="date">10 JUL 2019</span>
          <h3>LOREM IPSUM IS SIMPLY DUMMY TEXT.</h3>
          <p>Sed ut perspiciatis unde omnis iste natus error sit voluptatem accusantium doloremque.</p>
          <a href="#" class="btn">READ MORE</a>
        </div>
      </article>
      <article class="feature-card span2">
        <div class="photo-fill" role="img" aria-label="Container port at dusk seen from above" style="background:linear-gradient(160deg,#6a7fb8,#3a4c80 50%,#c77a54)"></div>
        <div class="shade"></div>
        <span class="date-pill">10 JUL 2019</span>
        <h3>LOREM IPSUM IS SIMPLY DUMMY TEXT.</h3>
        <p>Sed ut perspiciatis unde omnis iste natus error sit voluptatem accusantium doloremque.</p>
      </article>
    </div>
  </div>
</section>

<section class="featured">
  <div class="container">
    <h2 class="section-title">Featured Posts</h2>
    <div class="featured-grid">
      <article class="card">
        <div class="photo" style="background:linear-gradient(160deg,#b89a5c,#5a4a30)" role="img" aria-label="Forklift moving pallets in a warehouse"><span class="badge">10 JUL 2019</span></div>
        <div class="body">
          <h3>LOREM IPSUM IS SIMPLY DUMMY TEXT OF THE PRINTING</h3>
          <p>Sed ut perspiciatis unde omnis iste natus error sit.</p>
          <a href="#" class="btn">READ MORE</a>
        </div>
      </article>
      <article class="card">
        <div class="photo" style="background:linear-gradient(160deg,#4a78c0,#1c3a70)" role="img" aria-label="Stacked blue shipping containers"><span class="badge">10 JUL 2019</span></div>
        <div class="body">
          <h3>LOREM IPSUM IS SIMPLY DUMMY TEXT OF THE PRINTING</h3>
          <p>Sed ut perspiciatis unde omnis iste natus error sit.</p>
          <a href="#" class="btn">READ MORE</a>
        </div>
      </article>
      <article class="card">
        <div class="photo" style="background:linear-gradient(160deg,#8a8f98,#3c4048)" role="img" aria-label="Handshake over a delivery at a loading dock"><span class="badge">10 JUL 2019</span></div>
        <div class="body">
          <h3>LOREM IPSUM IS SIMPLY DUMMY TEXT OF THE PRINTING</h3>
          <p>Sed ut perspiciatis unde omnis iste natus error sit.</p>
          <a href="#" class="btn">READ MORE</a>
        </div>
      </article>
      <article class="card">
        <div class="photo" style="background:linear-gradient(160deg,#d45a7a,#3a5cb0 55%,#e0b040)" role="img" aria-label="Colourful containers in a port yard"><span class="badge">10 JUL 2019</span></div>
        <div class="body">
          <h3>LOREM IPSUM IS SIMPLY DUMMY TEXT OF THE PRINTING</h3>
          <p>Sed ut perspiciatis unde omnis iste natus error sit.</p>
          <a href="#" class="btn">READ MORE</a>
        </div>
      </article>
    </div>
  </div>
</section>

<section class="recent">
  <div class="container">
    <div class="recent-head">
      <h2 class="section-title">Recent Blog</h2>
      <div class="arrows">
        <svg width="12" height="18" viewBox="0 0 12 18"><path d="M10 2 3 9l7 7" fill="none" stroke="#777" stroke-width="2.5"/></svg>
        <svg width="12" height="18" viewBox="0 0 12 18"><path d="M2 2l7 7-7 7" fill="none" stroke="#333" stroke-width="2.5"/></svg>
      </div>
    </div>
    <div class="recent-grid">
      <article class="card">
        <div class="photo" style="background:linear-gradient(160deg,#9a6a50,#3e5a7c)" role="img" aria-label="Container yard with a worker in a safety vest"></div>
        <div class="body">
          <h3>LOREM IPSUM IS SIMPLY DUMMY TEXT.</h3>
          <p>Sed ut perspiciatis unde omnis iste natus error sit. type specimen book, keep into electronic typesetting.</p>
          <a href="#" class="btn">READ MORE</a>
        </div>
      </article>
      <article class="card">
        <div class="photo" style="background:linear-gradient(160deg,#a9c0dc,#54708f)" role="img" aria-label="Cargo aircraft parked on a runway"></div>
        <div class="body">
          <h3>LOREM IPSUM IS SIMPLY DUMMY TEXT.</h3>
          <p>Sed ut perspiciatis unde omnis iste natus error sit. type specimen book, keep into electronic typesetting.</p>
          <a href="#" class="btn">READ MORE</a>
        </div>
      </article>
      <article class="card">
        <div class="photo" style="background:linear-gradient(160deg,#cfd6dd,#6c7480)" role="img" aria-label="Freight loaded into the open nose of a cargo plane"></div>
        <div class="body">
          <h3>LOREM IPSUM IS SIMPLY DUMMY TEXT.</h3>
          <p>Sed ut perspiciatis unde omnis iste natus error sit. type specimen book, keep into electronic typesetting.</p>
          <a href="#" class="btn">READ MORE</a>
        </div>
      </article>
    </div>
  </div>
</section>

<section class="popular">
  <div class="container">
    <h2 class="section-title">Popular Posts</h2>
    <div class="popular-grid">
      <article class="feature-card big">
        <div class="photo-fill" role="img" aria-label="Airliners parked at an airport at dusk" style="background:linear-gradient(160deg,#2a3c78,#5a5e9a 50%,#c08a6a)"></div>
        <div class="shade"></div>
        <span class="date-pill">10 JUL 2019</span>
        <h3 style="font-size:24px;line-height:30px">LOREM IPSUM IS SIMPLY DUMMY TEXT.</h3>
        <p>Sed ut perspiciatis unde omnis iste natus error sit. type specimen book, keep into electronic typesetting.</p>
      </article>
      <article class="card">
        <div class="photo" style="background:linear-gradient(160deg,#c86a5a,#4a6a9a)" role="img" aria-label="Containers stacked at a harbour"></div>
        <div class="body"><span class="date">10 JUL 2019</span><h3>LOREM IPSUM IS SIMPLY DUMMY TEXT.</h3></div>
      </article>
      <article class="card">
        <div class="photo" style="background:linear-gradient(160deg,#a0a4a8,#50565e)" role="img" aria-label="Worker checking packages in a storage room"></div>
        <div class="body"><span class="date">10 JUL 2019</span><h3>LOREM IPSUM IS SIMPLY DUMMY TEXT.</h3></div>
      </article>
      <article class="card">
        <div class="photo" style="background:linear-gradient(160deg,#6a8ac0,#c07a4a)" role="img" aria-label="High-bay warehouse shelving"></div>
        <div class="body"><span class="date">10 JUL 2019</span><h3>LOREM IPSUM IS SIMPLY DUMMY TEXT.</h3></div>
      </article>
      <article class="card">
        <div class="photo" style="background:linear-gradient(160deg,#d07050,#5a7aa0)" role="img" aria-label="Rows of containers at a terminal"></div>
        <div class="body"><span class="date">10 JUL 2019</span><h3>LOREM IPSUM IS SIMPLY DUMMY TEXT.</h3></div>
      </article>
    </div>
  </div>
</section>

<footer class="site-footer">
  <div class="brand"><span class="brand-dot"></span>Veldax</div>
  <nav class="footer-nav">
    <a href="#">HOME</a><span class="sep">|</span>
    <a href="#">ABOUT US</a><span class="sep">|</span>
    <a href="#">VIDEOS</a><span class="sep">|</span>
    <a href="#">BLOG</a><span class="sep">|</span>
    <a href="#">CONTACT US</a>
  </nav>
  <div class="social"><span></span><span></span><span></span></div>
  <p class="copyright">Copyright 2019. All Rights Reserved</p>
</footer>

</body>
</html>
```